BrovaNest Landing Web Page

We need a web design for a new company head quartered in Philadelphia, PA with satellite offices in San Francisco, CA and New York, NY.
We have a logo and can provide the logo image file.
Here is some information on who we are:
BrovaNest
Growing information technology companies with experience
About Us: BrovaNest is an information technology incubator. We cultivate and groom start-ups from concept to reality to profitability. BrovaNest is managed and owned by entrepreneurs and technologists with proven start-up success. We seek to leverage synergies between our companies which foster innovation, stimulate creativity, increase productivity, streamline operational processes, and facilitate opportunity.
BrovaNest Companies:
• BrovaNest Health (should hyperlink to BrovaNest Health About Us section)
• BrovaNest IT Services and Staffing (should hyperlink to BrovaNest IT Services and Staffing About Us section)
Healthcare
Information Technology

```html
<!DOCTYPE html>
<html lang="en">
<head>
<meta charset="utf-8">
<title>BrovaNest</title>
<link rel="stylesheet" href="https://fonts.googleapis.com/css2?family=Cabin:wght@400;500;600&display=swap">
<style>
:root{
  --brand-dark:#0b6aa3;
  --brand:#1587c2;
  --brand-light:#37b6e3;
  --ink:#333;
  --muted:#777;
  --page:#f6f6f6;
  --panel:#f4f4f4;
  --card:#f7f7f7;
  --footer:#3b3b3b;
  --footer-dark:#2f2f2f;
}
*{margin:0;padding:0;box-sizing:border-box}
html,body{width:1145px;height:1200px;overflow:hidden}
body{position:relative;background:var(--page);font-family:"Cabin",sans-serif;color:var(--ink)}
.topbar{position:absolute;left:0;top:0;width:1145px;height:11px;background:var(--brand-dark);border-bottom:3px solid #fff}
.header{position:absolute;left:0;top:14px;width:1145px;height:602px;background:linear-gradient(#f3f3f3,#fbfbfb 30%,#fff)}
.logo{position:absolute;left:48px;top:56px;display:flex;align-items:center;gap:16px}
.logo-mark{width:68px;height:68px;background:var(--brand);border-radius:8px}
.logo-name{font-size:46px;font-weight:600;color:var(--brand)}
.follow{position:absolute;left:917px;top:83px;display:flex;align-items:center;gap:12px;font-size:13px;font-style:italic;color:var(--muted)}
.social{width:24px;height:24px;border:2px solid #888;border-radius:50%}
.nav{position:absolute;left:49px;top:169px;width:1047px;height:41px;border-radius:21px;background:linear-gradient(#1a93cf,#0b6aa3);display:flex;align-items:center;box-shadow:0 1px 2px rgba(0,0,0,.2)}
.nav a{height:41px;display:flex;align-items:center;justify-content:center;color:#fff;text-decoration:none;font-size:15px;border-right:1px solid rgba(255,255,255,.25)}
.nav .home{width:68px}
.search{position:absolute;right:20px;top:9px;width:207px;height:26px;border-radius:13px;background:#fff;box-shadow:inset 0 1px 3px rgba(0,0,0,.35)}
.search svg{position:absolute;right:8px;top:5px}
.hero{position:absolute;left:48px;top:241px;width:1047px;height:327px;border:1px solid #666;background:linear-gradient(90deg,#39424f 0%,#6c7a88 20%,#c9d9e6 42%,#e3eef6 70%,#eef4f8 100%);overflow:hidden}
.hero-caption{position:absolute;left:662px;top:216px;color:#333}
.hero-caption .line1{font-size:25px}
.hero-caption .line2{font-size:37px;margin-top:2px}
.slider-tab{position:absolute;left:442px;top:288px;width:200px;height:40px;background:linear-gradient(#555,#222);border-radius:14px 14px 0 0}
.dot{position:absolute;top:13px;width:15px;height:15px;border-radius:50%;background:#111;box-shadow:inset 0 1px 2px rgba(255,255,255,.2)}
.dot.active{background:#f2f2f2}
.hero-shadow{position:absolute;left:70px;top:568px;width:1005px;height:30px;background:radial-gradient(ellipse at top,rgba(0,0,0,.22),rgba(0,0,0,0) 70%)}
.content{position:absolute;left:0;top:616px;width:1145px;height:502px;background:var(--panel)}
.welcome{position:absolute;left:55px;top:30px;font-size:26px;font-weight:400;color:var(--brand)}
.welcome span{color:var(--brand-dark)}
.about{position:absolute;left:55px;top:82px;width:748px;font-size:13px;line-height:24px;text-align:justify;color:#333}
.company{position:absolute;left:858px;width:210px;display:flex;align-items:center;justify-content:center;text-align:center;color:#fff;text-decoration:none;font-size:17px;font-weight:500;line-height:24px;border-radius:3px;box-shadow:0 1px 3px rgba(0,0,0,.3);text-transform:uppercase}
.company.health{top:42px;height:41px;background:linear-gradient(#48c3ec,#1fa4d7)}
.company.it{top:105px;height:63px;background:linear-gradient(#1478b2,#0a5c90)}
.card{position:absolute;top:199px;height:276px;background:var(--card);border-radius:3px;box-shadow:0 1px 3px rgba(0,0,0,.18);padding:10px 22px}
.card h2{font-size:26px;font-weight:400;color:var(--brand);height:44px;line-height:44px}
.card h2 span{color:var(--brand-dark)}
.rule{width:231px;border-top:2px dotted #777;margin:6px 0 12px}
.card ul{list-style:none}
.card li{position:relative;padding-left:26px;font-size:14px;height:35px;line-height:22px}
.card li::before{content:"";position:absolute;left:6px;top:9px;width:5px;height:5px;border-radius:50%;background:#666}
.card p{font-size:12px;line-height:22px;color:#555;margin:0 0 12px 2px;text-align:justify}
.footer{position:absolute;left:0;top:1118px;width:1145px;height:82px;background:var(--footer-dark)}
.footer-links{height:46px;background:var(--footer);display:flex;align-items:center;justify-content:center;font-size:12px;color:#ddd}
.footer-links a{color:#eee;text-decoration:none}
.footer-links .sep{margin:0 12px}
.copyright{text-align:center;font-size:12px;color:#eee;line-height:36px}
</style>
</head>
<body>
<div class="topbar"></div>
<header class="header">
  <div class="logo">
    <div class="logo-mark"></div>
    <div class="logo-name">BrovaNest</div>
  </div>
  <div class="follow">Follow us with :
    <span class="social" role="img" aria-label="Social profile"></span>
    <span class="social" role="img" aria-label="Social profile"></span>
  </div>
</header>
<nav class="nav">
  <a class="home" href="#" aria-label="Home"><svg width="18" height="16" viewBox="0 0 18 16"><path d="M9 1 1 8h2.5v7h4v-4.5h3V15h4V8H17z" fill="#fff"/></svg></a>
  <a href="#" style="width:103px">Services</a>
  <a href="#" style="width:108px">Providers</a>
  <a href="#" style="width:104px">Members</a>
  <a href="#" style="width:83px">Blogs</a>
  <a href="#" style="width:112px">Contact us</a>
  <div class="search"><svg width="16" height="16" viewBox="0 0 16 16"><circle cx="6.5" cy="6.5" r="5" fill="none" stroke="#777" stroke-width="1.5"/><path d="M10 10l5 5" stroke="#777" stroke-width="1.5"/></svg></div>
</nav>
<section class="hero" role="img" aria-label="Smiling businesswoman beside a hand touching a glowing touchscreen interface">
  <div class="hero-caption">
    <div class="line1">Vivamus feugiat egestas lacus,</div>
    <div class="line2">vitae pulvinar tellus</div>
  </div>
  <div class="slider-tab">
    <span class="dot active" style="left:37px"></span>
    <span class="dot" style="left:66px"></span>
    <span class="dot" style="left:95px"></span>
    <span class="dot" style="left:123px"></span>
  </div>
</section>
<div class="hero-shadow"></div>
<main class="content">
  <h1 class="welcome">Welcome to <span>BrovaNest</span></h1>
  <p class="about">BrovaNest is an information technology incubator. We cultivate and groom start-ups from concept to reality to profitability. BrovaNest is managed and owned by entrepreneurs and technologists with proven start-up success. We seek to leverage synergies between our companies which foster innovation, stimulate creativity, increase productivity, streamline operational processes, and facilitate opportunity.</p>
  <a class="company health" href="#health-about">BrovaNest Health</a>
  <a class="company it" href="#it-about">BrovaNest IT Services<br>and Staffing</a>

  <article class="card" style="left:56px;width:282px">
    <h2>Our <span>IT Services</span></h2>
    <div class="rule"></div>
    <ul>
      <li>Pellentesque suscipit nisl a ligula</li>
      <li>Nunc et ipsum tortoreu</li>
      <li>Sed blandit leo eu tellus</li>
      <li>Vivamus feugiat egestas lacus</li>
      <li>Vestibulum in mauris sed massa</li>
      <li>Phasellus cursus convallis</li>
    </ul>
  </article>
  <article class="card" style="left:374px;width:282px">
    <h2>Our <span>Staffing Services</span></h2>
    <div class="rule"></div>
    <p>Sed ut perspiciatis unde omnis iste natus error sit voluptatem accusantium doloremque laudantium.</p>
    <ul>
      <li>Vivamus feugiat egestas lacus</li>
      <li>Vestibulum in mauris sed massa</li>
      <li>Phasellus cursus convallis</li>
    </ul>
  </article>
  <article class="card" style="left:691px;width:381px">
    <h2>Our <span>Health Services</span></h2>
    <div class="rule"></div>
    <ul>
      <li>Phasellus cursus convallis lacus, id porttitor</li>
      <li>Vivamus feugiat egestas lacus, vitae pulvinar</li>
      <li>Sed blandit leo eu tellus mattis ornare</li>
      <li>Nunc et ipsum tortor, eu porta dolor</li>
      <li>Pellentesque suscipit nisl a ligula tristique</li>
      <li>Nam molestie pretium magna, nec facilisis</li>
    </ul>
  </article>
</main>
<footer class="footer">
  <div class="footer-links">
    <a href="#">Home</a><span class="sep">|</span>
    <a href="#">About Us</a><span class="sep">|</span>
    <a href="#">Our services</a><span class="sep">|</span>
    <a href="#">Our companies</a><span class="sep">|</span>
    <a href="#">Latest News</a><span class="sep">|</span>
    <a href="#">Contact us</a><span class="sep">|</span>
    <a href="#">Member login</a><span class="sep">|</span>
    <a href="#">Sitemap</a>
  </div>
  <div class="copyright">Copyright © 2012 www.brovanest.com &nbsp; All rights reserved</div>
</footer>
</body>
</html>
```